Dedicated publishing company needs Book Cover with heart and soul

I am looking for a book cover design for a lovestory named "Kellnerinnen tanzen leiser" which means "waitresses dance quieter". It´s a funny, smart and heartwarming lovestory about a couple that seems to be too diverse - but which is meant to be.
He is a young and handsome movie star and she is the interior decorator of his film sets - an "average" looking slightly older woman with the heart in the right place.
Maybe some frames to reflect her work would be nice or some hollywood decor?
We are a dedicated publishing company who cares not only for the content but also for the design and we are open to any ideas! Looking forward to seeing your designs!

Target Market(s)

Women who enjoy good love stories

Industry/Entity Type

Publishing Company

Requirements
Must have
• The title: Kellnerinnen tanzen leiser
The autors name: Petra Lindqvist

Size of front 14,8 cm wide / 21 cm high ( with additional 3 mm around), spine approx 3 cm.
Front and back design

```html
<!DOCTYPE html>
<html lang="de">
<head>
<meta charset="utf-8">
<title>Kellnerinnen tanzen leiser – Cover</title>
<link rel="stylesheet" href="https://fonts.googleapis.com/css2?family=Della+Respira&family=Caveat+Brush&family=Arimo:wght@400&display=swap">
<style>
  :root {
    --paper: #ffffff;
    --ink: #141414;
    --accent-red: #e01b1b;
    --band-blue: #1598d6;
    --rule-black: #0c0c0c;
    --sketch-light: #f1f1f1;
    --sketch-mid: #c9c9c9;
    --spine-dark: #2e3136;
    --spine-mid: #4a4e54;
    --spine-light: #9a9ea4;
    --spine-w: 140px;
  }
  * { margin: 0; padding: 0; box-sizing: border-box; }
  html, body {
    width: 839px;
    height: 1200px;
    overflow: hidden;
    background: var(--paper);
  }
  .book {
    position: relative;
    width: 839px;
    height: 1200px;
    overflow: hidden;
    background: var(--paper);
  }
  .book__spine {
    position: absolute;
    top: 0;
    left: 0;
    width: var(--spine-w);
    height: 1200px;
    background: linear-gradient(to right,
      var(--spine-dark) 0%,
      var(--spine-mid) 25%,
      var(--spine-light) 42%,
      var(--spine-mid) 55%,
      var(--spine-dark) 100%);
  }
  .cover {
    position: absolute;
    top: 0;
    left: var(--spine-w);
    width: calc(839px - var(--spine-w));
    height: 1200px;
    background: var(--paper);
  }
  .cover__title {
    position: absolute;
    top: 70px;
    left: 0;
    width: 100%;
    text-align: center;
    font-family: "Della Respira", serif;
    font-weight: 400;
    font-size: 92px;
    line-height: 1.05;
    color: var(--ink);
    letter-spacing: 1px;
  }
  .cover__title span { display: block; }
  .cover__title .line-two { padding-left: 30px; }
  .cover__rose {
    position: absolute;
    top: 320px;
    left: 40px;
    width: 620px;
    height: 460px;
  }
  .cover__tagline {
    position: absolute;
    top: 840px;
    left: 0;
    width: 100%;
    text-align: center;
    font-family: "Caveat Brush", cursive;
    font-size: 104px;
    line-height: 1;
    color: var(--accent-red);
    letter-spacing: 3px;
  }
  .cover__rule {
    position: absolute;
    top: 1010px;
    left: 0;
    width: 100%;
    height: 12px;
    background: var(--rule-black);
  }
  .cover__band {
    position: absolute;
    top: 1022px;
    left: 0;
    width: 100%;
    height: 178px;
    background: var(--band-blue);
  }
  .cover__author {
    position: absolute;
    top: 20px;
    right: 40px;
    font-family: "Arimo", sans-serif;
    font-size: 28px;
    line-height: 1.2;
    color: var(--ink);
  }
</style>
</head>
<body>
  <div class="book">
    <div class="book__spine"></div>

    <main class="cover">
      <h1 class="cover__title">
        <span class="line-one">Kellnerinnen</span>
        <span class="line-two">tanzen leiser</span>
      </h1>

      <svg class="cover__rose" viewBox="0 0 620 460" role="img" aria-label="Pencil sketch of a large open rose blossom">
        <defs>
          <radialGradient id="roseTone" cx="50%" cy="45%" r="55%">
            <stop offset="0%" stop-color="#c9c9c9"/>
            <stop offset="100%" stop-color="#f1f1f1"/>
          </radialGradient>
        </defs>
        <ellipse cx="310" cy="230" rx="300" ry="225" fill="url(#roseTone)"/>
      </svg>

      <p class="cover__tagline">Love Story</p>

      <div class="cover__rule"></div>
      <div class="cover__band">
        <p class="cover__author">Petra Lindqvist</p>
      </div>
    </main>
  </div>
</body>
</html>
```